Conceptual Model Diagram for Replacing Medication with Behavior to Support Weight Loss Maintenance

Design a figure of a conceptual model that needs to be inserted into a word document for a PSF grant. This conceptual model illustrates how behavioral strategies can replace the regulatory functions lost after AOM discontinuation. The intervention targets three core vulnerabilities—appetite resurgence, metabolic inflexibility, and suboptimal mindstate—through the domains of Food, Physical Activity, and Mind. Sustained weight loss maintenance occurs at the intersection of these domains. The intervention is delivered within a design framework that makes behaviors easier to perform, aligns them with identity, and reinforces them through virtual support and community, ensuring real-world feasibility and long-term adherence.
Target Market(s)
PSF reviewers
Industry/Entity Type
academic
Other font styles liked:
- arial
Requirements
Must have
- see my attached description

```html
<!DOCTYPE html>
<html lang="en">
<head>
<meta charset="utf-8">
<title>Conceptual Model – Sustained Weight Loss Maintenance</title>
<link href="https://fonts.googleapis.com/css2?family=Montserrat:wght@400;500;600;700;800&display=swap" rel="stylesheet">
<style>
  :root {
    --teal-food: #1f9e8a;
    --teal-mind: #5fc3ad;
    --teal-activity: #22b395;
    --teal-overlap: #0e7d6d;
    --teal-dark: #0b5f54;
    --ink: #1d2b2a;
    --muted: #4a5a58;
    --white: #ffffff;
    --caption-bg: #eef2f1;
    --ring: #7ccfbd;
  }
  html, body {
    margin: 0;
    padding: 0;
    overflow: hidden;
    background: var(--white);
  }
  .canvas {
    width: 759px;
    height: 1200px;
    position: relative;
    overflow: hidden;
    font-family: "Montserrat", Arial, sans-serif;
    color: var(--ink);
  }
  .model {
    position: absolute;
    left: 0;
    top: 0;
    width: 759px;
    height: 1010px;
  }
  .domain-label { fill: var(--white); font-weight: 800; letter-spacing: 0.5px; }
  .overlap-label { fill: var(--white); font-weight: 600; }
  .core-label { fill: var(--teal-dark); font-weight: 800; }
  .framework-title { fill: var(--teal-dark); font-weight: 800; letter-spacing: 0.6px; }
  .framework-item { fill: var(--muted); font-weight: 500; }
  .icon-slot { fill: rgba(255,255,255,0.25); }
  .caption {
    position: absolute;
    left: 60px;
    top: 1028px;
    width: 639px;
    box-sizing: border-box;
    padding: 18px 26px 20px;
    background: var(--caption-bg);
    border-radius: 6px;
    text-align: center;
  }
  .caption-title {
    margin: 0 0 8px;
    font-size: 11px;
    font-weight: 800;
    letter-spacing: 0.8px;
    color: var(--teal-dark);
  }
  .caption-body {
    margin: 0;
    font-size: 10.5px;
    line-height: 1.5;
    color: var(--muted);
  }
</style>
</head>
<body>
<div class="canvas">
  <svg class="model" viewBox="0 0 759 1010" xmlns="http://www.w3.org/2000/svg" xmlns:xlink="http://www.w3.org/1999/xlink">
    <defs>
      <clipPath id="clip-food"><circle cx="380" cy="160" r="125"/></clipPath>
      <clipPath id="clip-mind"><circle cx="310" cy="280" r="125"/></clipPath>

      <g id="venn-model">
        <circle cx="380" cy="160" r="125" fill="var(--teal-food)"/>
        <circle cx="310" cy="280" r="125" fill="var(--teal-mind)"/>
        <circle cx="450" cy="280" r="125" fill="var(--teal-activity)"/>
        <g clip-path="url(#clip-food)">
          <circle cx="310" cy="280" r="125" fill="var(--teal-overlap)"/>
          <circle cx="450" cy="280" r="125" fill="var(--teal-overlap)"/>
        </g>
        <g clip-path="url(#clip-mind)">
          <circle cx="450" cy="280" r="125" fill="var(--teal-overlap)"/>
        </g>
        <g clip-path="url(#clip-food)">
          <g clip-path="url(#clip-mind)">
            <circle cx="450" cy="280" r="125" fill="var(--white)"/>
          </g>
        </g>
        <g fill="none" stroke="var(--white)" stroke-width="2">
          <circle cx="380" cy="160" r="125"/>
          <circle cx="310" cy="280" r="125"/>
          <circle cx="450" cy="280" r="125"/>
        </g>

        <text class="domain-label" x="380" y="124" font-size="24" text-anchor="middle">FOOD</text>
        <text class="domain-label" x="258" y="342" font-size="24" text-anchor="middle">MIND</text>
        <text class="domain-label" x="505" y="326" font-size="20" text-anchor="middle">PHYSICAL</text>
        <text class="domain-label" x="505" y="349" font-size="20" text-anchor="middle">ACTIVITY</text>

        <text class="overlap-label" x="302" y="200" font-size="10" text-anchor="middle">Suboptimal</text>
        <text class="overlap-label" x="305" y="213" font-size="10" text-anchor="middle">Mindstate</text>
        <text class="overlap-label" x="458" y="200" font-size="10" text-anchor="middle">Appetite</text>
        <text class="overlap-label" x="455" y="213" font-size="10" text-anchor="middle">Resurgence</text>
        <text class="overlap-label" x="380" y="312" font-size="10" text-anchor="middle">Metabolic</text>
        <text class="overlap-label" x="380" y="325" font-size="10" text-anchor="middle">Inflexibility</text>

        <text class="core-label" x="380" y="229" font-size="8.5" text-anchor="middle">SUSTAINED</text>
        <text class="core-label" x="380" y="243" font-size="11" text-anchor="middle">WEIGHT</text>
        <text class="core-label" x="380" y="264" font-size="19" text-anchor="middle">LOSS</text>
        <text class="core-label" x="380" y="276" font-size="7.5" text-anchor="middle">MAINTENANCE</text>
      </g>
    </defs>

    <!-- Main model -->
    <g class="venn-main">
      <use href="#venn-model" xlink:href="#venn-model" transform="translate(380 290) scale(1.35) translate(-380 -240)"/>
      <circle class="icon-slot" cx="380" cy="104" r="26" role="img" aria-label="Food icon"/>
      <circle class="icon-slot" cx="260" cy="369" r="26" role="img" aria-label="Brain icon"/>
      <circle class="icon-slot" cx="503" cy="347" r="26" role="img" aria-label="Exercise icon"/>
    </g>

    <!-- Delivery framework -->
    <g class="framework">
      <text class="framework-title" x="380" y="672" font-size="16" text-anchor="middle">MAKE IT EASY</text>
      <text class="framework-item" x="380" y="694" font-size="11" text-anchor="middle">Habits  •  Routines  •  Environment  •  Low Friction</text>

      <circle cx="380" cy="850" r="140" fill="none" stroke="var(--ring)" stroke-width="2" stroke-dasharray="4 6"/>

      <text class="framework-title" x="150" y="842" font-size="15" text-anchor="middle">VIRTUAL SUPPORT</text>
      <text class="framework-title" x="150" y="861" font-size="15" text-anchor="middle">AND SOCIAL</text>
      <text class="framework-title" x="150" y="880" font-size="15" text-anchor="middle">CONNECTION</text>
      <text class="framework-item" x="150" y="904" font-size="11" text-anchor="middle">• Accessibility</text>
      <text class="framework-item" x="150" y="920" font-size="11" text-anchor="middle">• Community</text>
      <text class="framework-item" x="150" y="936" font-size="11" text-anchor="middle">• Shared Accountability</text>

      <text class="framework-title" x="615" y="852" font-size="15" text-anchor="middle">ALIGN WITH</text>
      <text class="framework-title" x="615" y="871" font-size="15" text-anchor="middle">IDENTITY</text>
      <text class="framework-item" x="615" y="895" font-size="11" text-anchor="middle">• Self-Concept</text>
      <text class="framework-item" x="615" y="911" font-size="11" text-anchor="middle">• Internalization</text>
      <text class="framework-item" x="615" y="927" font-size="11" text-anchor="middle">• Maintain IT Model</text>
    </g>

    <!-- Small model inside framework -->
    <g class="venn-small">
      <use href="#venn-model" xlink:href="#venn-model" transform="translate(380 854) scale(0.608) translate(-380 -240)"/>
    </g>
  </svg>

  <section class="caption">
    <h2 class="caption-title">FIGURE CAPTION FOR GRANT APPLICATION</h2>
    <p class="caption-body">This conceptual model illustrates how behavioral strategies can replace the regulatory functions lost after AOM discontinuation. The intervention targets three core vulnerabilities—appetite resurgence, metabolic inflexibility, and suboptimal mindstate—through the domains of Food, Physical Activity, and Mind. Sustained weight loss maintenance occurs at the intersection of these domains. The intervention is delivered within a design framework that makes behaviors easier to perform, aligns them with identity, and reinforces them through virtual support and community, ensuring real-world feasibility and long-term adherence.</p>
  </section>
</div>
</body>
</html>
```